Business Card for Coach - ready to print

Design Business Card ready to order prints www.larsholm.coach

* An Overview / Background of the Business & Services
· Coaching
· Personal growth
* The Target Market / Audience you are trying to reach
· private person in different roles (self, familiy, business role)s
* Design Specifics; any preferences or ideas for Style, Colour, Imagery, etc
· See www.larsholm.coach
· "simple" design
· (small) element of surprise / unusual element

* Information that will be placed in the Business Card
· Beratung und Coaching
· Address: Lars Holm, Kesselgasse 7, CH-8517 Winterthur, Mobile +41 76 254 60 31
* Do you have an existing website or Facebook page where designers can learn more about your company?
· larsholm.coach

Target Market(s)

private person in different roles (self, familiy, business role)

Industry/Entity Type

Life Coaching

Contact Information for Business Card

Lars Holm
Kesselgasse 7
CH-8517 Winterthur

Mobile: +41 76 254 60 31
Email: laho@mailvale.ch
www.larsholm.coach

Font styles to use
Sans Serif

Colors

Designer to choose colors to be used in the design.

Requirements
Must have
• "simple" design
• element of surprise / unusual element
• Beratung & Coaching
• see www.larsholm.coach for colors and so...
Nice to have
• TA Symbol (three rings on top of each other) - unsual presentation
• QR Code of Website (see if it fits in and still looks good).

```html
<!DOCTYPE html>
<html lang="de">
<head>
<meta charset="utf-8">
<title>Lars Holm – Visitenkarte</title>
<link rel="stylesheet" href="https://fonts.googleapis.com/css2?family=Open+Sans:wght@400;700&display=swap">
<style>
  :root {
    --brand-blue: #028db7;
    --card-white: #ffffff;
    --ink: #4a4a4a;
    --backdrop: #9b9b9b;
  }
  * { margin: 0; padding: 0; box-sizing: border-box; }
  html, body {
    width: 1133px; height: 1200px; overflow: hidden;
    background: var(--backdrop);
    font-family: "Open Sans", sans-serif;
  }
  .card {
    position: absolute; left: 219px; width: 694px; height: 396px;
  }
  .card--front { top: 153px; background: var(--brand-blue); display: flex; align-items: center; justify-content: center; }
  .card--back { top: 649px; background: var(--card-white); }
  .front-name {
    color: var(--card-white); font-weight: 700; font-size: 59px;
    letter-spacing: 0.5px; text-transform: uppercase; line-height: 1;
  }
  .back-name {
    position: absolute; right: 384px; top: 183px;
    color: var(--brand-blue); font-weight: 700; font-size: 29px;
    text-transform: uppercase; line-height: 1; white-space: nowrap;
  }
  .divider {
    position: absolute; left: 333px; top: 134px; width: 1.5px; height: 130px;
    background: var(--brand-blue);
  }
  .contact {
    position: absolute; left: 352px; top: 128px;
    color: var(--ink); font-size: 19px; line-height: 25px;
  }
  .address { margin-bottom: 12px; }
  .contact-line { display: flex; align-items: center; white-space: nowrap; }
  .contact-line svg { width: 16px; height: 16px; margin-right: 5px; fill: var(--brand-blue); flex: none; }
</style>
</head>
<body>
  <section class="card card--front">
    <h1 class="front-name">Lars Holm</h1>
  </section>

  <section class="card card--back">
    <div class="back-name">Lars Holm</div>
    <div class="divider"></div>
    <div class="contact">
      <div class="address">Kesselgasse 7<br>CH-8517 Winterthur</div>
      <div class="contact-line">
        <svg viewBox="0 0 16 16" aria-hidden="true"><path d="M3.5 1.5l2.5 2.8-1.5 1.6c.9 2 2.4 3.5 4.4 4.4l1.6-1.5 2.8 2.5-1.6 2.2C6.7 13.2 2.8 9.3 1.3 3.1z"/><path d="M10 1.5a4.5 4.5 0 0 1 4.5 4.5h-1.2A3.3 3.3 0 0 0 10 2.7z"/></svg>
        +41 76 254 60 31
      </div>
      <div class="contact-line">
        <svg viewBox="0 0 16 16" aria-hidden="true"><path d="M2 5h12v8H2z M2 5l6 4 6-4" fill="var(--brand-blue)"/><path d="M2.5 5.5l5.5 3.7 5.5-3.7" fill="none" stroke="#fff" stroke-width="1.1"/></svg>
        laho@mailvale.ch
      </div>
      <div class="contact-line">
        <svg viewBox="0 0 16 16" aria-hidden="true"><circle cx="8" cy="8.5" r="6.5"/><path d="M5 5c1.5.5 2 2 1 3s.5 2.5 1.5 3M10 4c0 1.5 1.5 1.5 2.5 2" fill="none" stroke="#fff" stroke-width="1.1"/></svg>
        www.larsholm.coach
      </div>
    </div>
  </section>
</body>
</html>
```